Business Cards - New Logo Rebranding

Hello We know have a red and blue logo and are looking to create new cards. We are looking for the best creativity of the new logo merged with some of the existing artwork provided.

Target Market(s)

Realtors

Industry/Entity Type

Real Estate

Contact Information for Business Card

New logo with rebranded colors

Requirements
Must have
• Creative use of the new logo

```html
<!DOCTYPE html>
<html lang="en">
<head>
<meta charset="utf-8">
<title>Summit Group Business Cards</title>
<link href="https://fonts.googleapis.com/css2?family=Poppins:wght@400;500;600;700;800&display=swap" rel="stylesheet">
<style>
  :root {
    --bg: #ece8e6;
    --blue: #1470b8;
    --red: #e03a40;
    --ink: #111;
    --white: #fff;
    --border: #b9b9b9;
  }
  html, body { margin: 0; padding: 0; width: 1200px; height: 1200px; overflow: hidden; background: var(--bg); font-family: "Poppins", sans-serif; }
  .canvas { position: relative; width: 1200px; height: 1200px; }
  .side-label { position: absolute; font-weight: 700; font-size: 21px; color: var(--ink); transform: translateX(-50%); margin: 0; }
  .card { position: absolute; top: 505px; width: 490px; height: 291px; background: var(--white); border: 1px solid var(--border); box-sizing: border-box; overflow: hidden; }
  .card--front { left: 94px; }
  .card--back { left: 619px; }
  .brand { position: absolute; width: 160px; text-align: center; transform: translateX(-50%); }
  .brand__mark { display: block; margin: 0 auto; width: 58px; height: 58px; border-radius: 50%; background: var(--blue); border: 3px solid var(--red); box-sizing: border-box; }
  .brand__name { display: block; margin-top: 5px; font-weight: 800; font-size: 14px; letter-spacing: 0.5px; color: var(--blue); line-height: 1; }
  .brand__tag { display: block; margin-top: 2px; font-weight: 600; font-size: 5px; letter-spacing: 0.4px; color: var(--blue); border-top: 1px solid var(--red); padding-top: 1px; width: 92px; margin-left: auto; margin-right: auto; }
  .person { position: absolute; left: 48px; top: 154px; }
  .person__name { font-weight: 700; font-size: 17px; color: var(--blue); margin: 0; line-height: 1.1; }
  .person__title { font-weight: 500; font-size: 10px; color: var(--red); margin: 4px 0 0; }
  .divider { position: absolute; left: 228px; top: 148px; width: 2px; height: 73px; background: var(--blue); }
  .contacts { position: absolute; left: 257px; top: 148px; margin: 0; padding: 0; list-style: none; }
  .contacts li { display: flex; align-items: center; height: 15px; font-size: 10px; font-weight: 500; color: var(--blue); }
  .contacts svg { width: 10px; height: 10px; margin-right: 6px; fill: var(--blue); }
  .services { position: absolute; left: 0; right: 0; top: 242px; height: 24px; background: var(--red); color: var(--white); font-weight: 500; font-size: 12px; display: flex; align-items: center; justify-content: center; letter-spacing: 0.2px; }
  .why-panel { position: absolute; left: 185px; top: 0; right: 0; height: 224px; background: var(--blue); color: var(--white); }
  .headline { position: absolute; left: 0; top: 13px; width: 290px; height: 31px; background: var(--white); color: var(--red); font-size: 12.5px; font-weight: 500; display: flex; align-items: center; padding-left: 11px; box-sizing: border-box; white-space: nowrap; }
  .headline strong { font-weight: 800; margin-right: 4px; }
  .why-title { position: absolute; left: 12px; top: 57px; margin: 0; font-size: 11.5px; font-weight: 500; }
  .benefits { position: absolute; left: 12px; top: 86px; margin: 0; padding: 0; list-style: none; }
  .benefits li { display: flex; align-items: center; height: 22px; font-size: 9px; font-weight: 500; white-space: nowrap; }
  .benefits svg { width: 9px; height: 9px; margin-right: 9px; stroke: var(--white); fill: none; stroke-width: 2; }
  .reviews { position: absolute; left: 185px; right: 0; top: 232px; text-align: center; margin: 0; color: var(--red); font-weight: 700; font-size: 12.5px; line-height: 1.35; }
  .badge { position: absolute; }
</style>
</head>
<body>
<div class="canvas">
  <p class="side-label" style="left:354px; top:435px;">FRONT</p>
  <p class="side-label" style="left:808px; top:456px;">BACK</p>

  <section class="card card--front">
    <div class="brand" style="left:244px; top:39px;">
      <span class="brand__mark"></span>
      <span class="brand__name">SUMMIT GROUP</span>
      <span class="brand__tag">INSPECTION PROFESSIONALS</span>
    </div>
    <div class="person">
      <p class="person__name">Dana Marlowe</p>
      <p class="person__title">Certified Mold Inspector</p>
    </div>
    <div class="divider"></div>
    <ul class="contacts">
      <li><svg viewBox="0 0 10 10"><path d="M2 0.5 L3.6 2.6 L2.8 3.6 Q4 6 6.4 7.2 L7.4 6.4 L9.5 8 L8.4 9.5 Q3 9 0.5 1.6 Z"/></svg>800.555.0142</li>
      <li><svg viewBox="0 0 10 10"><rect x="2.5" y="0.5" width="5" height="9" rx="1" fill="none" stroke="#1470b8" stroke-width="1.2"/><circle cx="5" cy="8" r="0.6"/></svg>562.555.0187</li>
      <li><svg viewBox="0 0 10 10"><rect x="0.5" y="1.5" width="9" height="7" fill="none" stroke="#1470b8" stroke-width="1.2"/><path d="M0.5 1.5 L5 5.5 L9.5 1.5" fill="none" stroke="#1470b8" stroke-width="1.2"/></svg>danamarlowe@summitinspect.com</li>
      <li><svg viewBox="0 0 10 10"><circle cx="5" cy="5" r="4.4" fill="none" stroke="#1470b8" stroke-width="1.1"/><ellipse cx="5" cy="5" rx="2" ry="4.4" fill="none" stroke="#1470b8" stroke-width="1"/><path d="M0.6 5 H9.4" stroke="#1470b8" stroke-width="1"/></svg>www.SummitInspect.com</li>
    </ul>
    <div class="services">HOME • SEWER • MOLD • COMMERCIAL • TERMITE • ROOF</div>
  </section>

  <section class="card card--back">
    <div class="brand" style="left:100px; top:39px;">
      <span class="brand__mark"></span>
      <span class="brand__name">SUMMIT GROUP</span>
      <span class="brand__tag">INSPECTION PROFESSIONALS</span>
    </div>

    <svg class="badge" style="left:0; top:0;" width="185" height="291" viewBox="0 0 185 291" role="img" aria-label="Certification and review listing badges">
      <circle cx="56" cy="223" r="13" fill="#c9302f" stroke="#1c3f7a" stroke-width="3"/>
      <circle cx="96" cy="223" r="13" fill="#b89a2e" stroke="#2a4a7a" stroke-width="3"/>
      <circle cx="134" cy="223" r="13" fill="#2d2d2d" stroke="#b89a2e" stroke-width="3"/>
      <rect x="40" y="253" width="46" height="18" rx="3" fill="#2b3a78"/>
      <rect x="99" y="253" width="26" height="18" rx="2" fill="#d32323"/>
      <circle cx="146" cy="262" r="8" fill="#e46f2a"/>
    </svg>

    <div class="why-panel">
      <div class="headline"><strong>CALIFORNIA'S #1</strong> INSPECTION COMPANY!</div>
      <p class="why-title">Why Choose the Summit Group...</p>
      <ul class="benefits">
        <li><svg viewBox="0 0 10 10"><path d="M1 5.5 L4 8.5 L9 1.5"/></svg>Performing Inspections Since 1984</li>
        <li><svg viewBox="0 0 10 10"><path d="M1 5.5 L4 8.5 L9 1.5"/></svg>HomeCert Certified Master/ Professional Inspectors®</li>
        <li><svg viewBox="0 0 10 10"><path d="M1 5.5 L4 8.5 L9 1.5"/></svg>500,000+ Inspections Completed Statewide</li>
        <li><svg viewBox="0 0 10 10"><path d="M1 5.5 L4 8.5 L9 1.5"/></svg>Request of Repairs Fixcost Report</li>
        <li><svg viewBox="0 0 10 10"><path d="M1 5.5 L4 8.5 L9 1.5"/></svg>90-Day Inspection Guarantees</li>
        <li><svg viewBox="0 0 10 10"><path d="M1 5.5 L4 8.5 L9 1.5"/></svg>AirCert Drone Licensed Roof Inspectors upon request</li>
      </ul>
    </div>
    <p class="reviews">5,000+ 5-Star<br>Reviews on Searchly &amp; Ratewell</p>
  </section>
</div>
</body>
</html>
```